Paw Summit Co business card

I need a business card design for a dog training company in Toronto called Paw Summit Co. My training is unique, outdoor training that helps people create a better bond with their dog through communication and understanding their dog's true nature. I do not use treats - but communication and praise for the dog.

I help people create a better life for them and their dog. From puppy training right through to seniors, I offer both group classes called Curbside Poise Course as well as in-home private sessions.

I believe that having a dog is a lifestyle, so I encourage clients to incorporate their dog into their active life. Outdoor activities such as hiking, mental stimulation, proper care and healthy food for their dog are all keys to a healthy and happy dog.

I would like a fresh and modern look that works with my logo. I would like to convey fun, confidence and happiness.

My services are premium services. I am a Certified Dog Trainer, and offer value for money, but my prices are higher than other trainers.
Updates

Thank you to everyone who submitted designs! I'm so impressed with the level of creativity and the options that you all have given me. It will be a difficult choice for sure. As this was my first experience with Art Huddle - it has been a great one.

maren.

Industry/Entity Type

Communication

Requirements
Must have
• Maren Quill, CTE
Certified Trainer Educator
maren@pawsummitco.ca
555-318-0472
pawsummitco.ca

Prefer a double sided card.
Must have Paw Summit Co logo. File attached. I do have a stroke logo for a dark background as well.

Must only use the fonts and colours as outlined in my brand guidelines, which are attached.
Should not have
• no cheesy pet images
do not use the tongue as an element outside of the logo
minimize the use of pink - can be used as an accent colour but should not be a main colour

```html
<!DOCTYPE html>
<html lang="en">
<head>
<meta charset="utf-8">
<title>Paw Summit Co – Business Card</title>
<link rel="stylesheet" href="https://fonts.googleapis.com/css2?family=Didact+Gothic&family=Montserrat:wght@700;800&display=swap">
<style>
  :root {
    --stage: #eceeea;
    --card-white: #ffffff;
    --card-dark: #4b4a4d;
    --brand-green: #8dba3f;
    --ink: #3a393c;
    --ink-soft: #2f2f31;
    --faint-mark: #5c5a5e;
  }
  * { box-sizing: border-box; margin: 0; padding: 0; }
  html, body {
    width: 1200px; height: 798px; overflow: hidden;
    background: var(--stage);
  }
  .sheet {
    width: 1200px; height: 798px;
    display: flex; align-items: center; justify-content: center; gap: 40px;
  }
  .card {
    width: 540px; height: 309px; position: relative; overflow: hidden;
    box-shadow: 0 10px 28px rgba(0,0,0,.16);
  }

  /* Front */
  .card-front { background: var(--card-white); }
  .brand-name {
    position: absolute; left: 30px; top: 42px; width: 210px;
    font: 800 38px/0.98 "Montserrat", sans-serif;
    color: var(--ink);
    letter-spacing: -0.5px;
  }
  .identity { position: absolute; left: 280px; top: 102px; }
  .person-name {
    font: 700 21px/1.1 "Montserrat", sans-serif; color: var(--ink);
  }
  .person-title {
    margin-top: 8px;
    font: 700 10.5px/1 "Montserrat", sans-serif; color: var(--brand-green);
    letter-spacing: .6px; text-transform: uppercase;
  }
  .contact { position: absolute; left: 280px; top: 196px; }
  .contact-line {
    font: 16px/1.5 "Didact Gothic", sans-serif; color: var(--ink-soft);
  }
  .contact-web {
    margin-top: 4px;
    font: 700 19px/1.2 "Montserrat", sans-serif; color: var(--brand-green);
  }

  /* Back */
  .card-back { background: var(--card-dark); }
  .back-mark {
    position: absolute; left: 26px; top: 60px;
    font: 800 64px/0.92 "Montserrat", sans-serif;
    color: var(--faint-mark);
    letter-spacing: -1px;
  }
  .certificate-badge { position: absolute; right: 40px; top: 30px; }
  .tagline {
    position: absolute; right: 36px; bottom: 32px;
    font: 30px/1 "Didact Gothic", sans-serif; color: var(--brand-green);
  }
</style>
</head>
<body>
  <main class="sheet">
    <section class="card card-front" aria-label="Card front">
      <div class="brand-name">Paw Summit Co</div>
      <div class="identity">
        <p class="person-name">Maren Quill, CTE</p>
        <p class="person-title">Certified Trainer Educator</p>
      </div>
      <div class="contact">
        <p class="contact-line">maren@pawsummitco.ca</p>
        <p class="contact-line">555-318-0472</p>
        <p class="contact-web">pawsummitco.ca</p>
      </div>
    </section>

    <section class="card card-back" aria-label="Card back">
      <div class="back-mark" aria-hidden="true">Paw<br>Summit Co</div>
      <svg class="certificate-badge" width="96" height="96" viewBox="0 0 96 96" role="img" aria-label="Certification badge">
        <circle cx="48" cy="48" r="45" fill="none" stroke="var(--brand-green)" stroke-width="3"/>
      </svg>
      <p class="tagline">Training for life</p>
    </section>
  </main>
</body>
</html>
```